Contemporary Media Company with Logo Needs Business Card Design

Need a modern card design for a full service digital media company using the logo included. Also want the info below on the card. Probably list the services on the card back to save space for the front. Want something contemporary to impress prospective clients. You may want to submit both a somewhat more conservative design, and then a more wild one.
General Info: (this phrase need not be on the card)
Ned Parlow
Founder and CEO
949-612-4830
ned@vontaramedia.example
vontaramedia.example
Services: (this word need not be on the card)
Content & Experience Strategy
Brand Development
Search Engine Optimization
Website Design
Website Operation
Social Media Integration
Complete Video Solutions
Updates
Industry/Entity Type
Business
Contact Information for Business Card
Ned Parlow
Founder and CEO
949-612-4830
ned@vontaramedia.example
vontaramedia.example
Brand Development
Website Design
Website Operation
Social Media Integration
Complete Video Solutions
Look and feel
Each slider illustrates characteristics of the customer's brand and the style your logo design should communicate.

```html
<!DOCTYPE html>
<html lang="en">
<head>
<meta charset="utf-8">
<title>Vontara Media – Business Card</title>
<link rel="stylesheet" href="https://fonts.googleapis.com/css2?family=PT+Sans:wght@400;700&display=swap">
<style>
  :root {
    --page-bg: #d6d6d6;
    --card-light-top: #f4f4f4;
    --card-light-bottom: #d9d9d9;
    --card-dark: #58595b;
    --card-dark-edge: #4f5052;
    --accent-orange: #e06a1e;
    --ink-gray: #5b5b5b;
    --ink-black: #1a1a1a;
    --ink-white: #ffffff;
    --name-dark: #141414;
  }
  * { margin: 0; padding: 0; box-sizing: border-box; }
  html, body {
    width: 1189px;
    height: 1200px;
    overflow: hidden;
    background: var(--page-bg);
    font-family: "PT Sans", sans-serif;
  }
  .card {
    position: absolute;
    left: 140px;
    width: 916px;
    height: 524px;
    overflow: hidden;
    box-shadow: 4px 6px 10px rgba(0,0,0,0.35);
  }
  .card--front { top: 45px; }
  .card--back {
    top: 623px;
    background: radial-gradient(ellipse at 55% 0%, #ffffff 0%, var(--card-light-top) 35%, var(--card-light-bottom) 100%);
  }

  /* Front */
  .brand-panel {
    position: absolute;
    left: 0; top: 0;
    width: 100%; height: 278px;
    background: linear-gradient(180deg, var(--card-light-bottom) 0%, var(--card-light-top) 100%);
  }
  .brand {
    position: absolute;
    left: 140px; top: 108px;
    display: flex;
    align-items: center;
    gap: 26px;
  }
  .brand__square {
    width: 54px; height: 54px;
    background: var(--accent-orange);
  }
  .brand__name {
    font-size: 58px;
    font-weight: 400;
    letter-spacing: 6px;
    text-transform: uppercase;
    color: var(--ink-gray);
    line-height: 1;
  }
  .accent-stripe {
    position: absolute;
    left: 0; top: 278px;
    width: 100%; height: 13px;
    background: var(--accent-orange);
  }
  .contact-panel {
    position: absolute;
    left: 0; top: 291px;
    width: 100%; height: 233px;
    background: radial-gradient(ellipse at 40% 60%, #5e5f61 0%, var(--card-dark) 55%, var(--card-dark-edge) 100%);
  }
  .person {
    position: absolute;
    left: 104px; top: 60px;
  }
  .person__name {
    font-size: 34px;
    color: var(--name-dark);
    line-height: 1.1;
  }
  .person__title {
    font-size: 26px;
    color: var(--ink-white);
    margin-top: 8px;
  }
  .divider {
    position: absolute;
    left: 383px; top: 57px;
    width: 2px; height: 108px;
    background: var(--ink-white);
  }
  .contact-list {
    position: absolute;
    left: 466px; top: 56px;
    list-style: none;
  }
  .contact-list li {
    display: flex;
    align-items: center;
    height: 35px;
    font-size: 26px;
    color: var(--ink-white);
  }
  .contact-list svg {
    width: 18px; height: 18px;
    margin-right: 14px;
    flex: none;
  }

  /* Back */
  .services {
    position: absolute;
    left: 242px; top: 130px;
    list-style: none;
  }
  .services li {
    position: relative;
    padding-left: 26px;
    height: 38.5px;
    font-size: 27px;
    line-height: 38px;
    color: var(--ink-black);
  }
  .services li::before {
    content: "";
    position: absolute;
    left: 0; top: 16px;
    width: 8px; height: 8px;
    border-radius: 50%;
    background: var(--ink-black);
  }
</style>
</head>
<body>

<section class="card card--front">
  <div class="brand-panel">
    <div class="brand">
      <span class="brand__square"></span>
      <span class="brand__name">Vontara Media</span>
    </div>
  </div>
  <div class="accent-stripe"></div>
  <div class="contact-panel">
    <div class="person">
      <p class="person__name">Ned Parlow</p>
      <p class="person__title">Founder and CEO</p>
    </div>
    <div class="divider"></div>
    <ul class="contact-list">
      <li>
        <svg viewBox="0 0 18 18" aria-hidden="true">
          <rect width="18" height="18" rx="2" fill="#ffffff"/>
          <path d="M5 3.5 L7.2 3.5 L8 6.5 L6.6 7.6 Q7.6 10.2 10.4 11.4 L11.5 10 L14.5 10.8 L14.5 13 Q13.5 14.5 11.5 14 Q5.5 12 4 6 Q3.8 4.2 5 3.5 Z" fill="#58595b"/>
        </svg>
        949-612-4830
      </li>
      <li>
        <svg viewBox="0 0 18 18" aria-hidden="true">
          <rect width="18" height="18" rx="2" fill="#ffffff"/>
          <rect x="3" y="5" width="12" height="8" fill="none" stroke="#58595b" stroke-width="1.4"/>
          <path d="M3 5 L9 10 L15 5" fill="none" stroke="#58595b" stroke-width="1.4"/>
        </svg>
        ned@vontaramedia.example
      </li>
      <li>
        <svg viewBox="0 0 18 18" aria-hidden="true">
          <rect width="18" height="18" rx="2" fill="#ffffff"/>
          <circle cx="9" cy="9" r="5.5" fill="none" stroke="#58595b" stroke-width="1.4"/>
          <ellipse cx="9" cy="9" rx="2.3" ry="5.5" fill="none" stroke="#58595b" stroke-width="1.1"/>
          <path d="M3.5 9 H14.5" stroke="#58595b" stroke-width="1.1"/>
        </svg>
        www.vontaramedia.example
      </li>
    </ul>
  </div>
</section>

<section class="card card--back">
  <ul class="services">
    <li>Website Design</li>
    <li>Website Operation</li>
    <li>Brand Development</li>
    <li>Social Media Integration</li>
    <li>Complete Video Solutions</li>
    <li>Search Engine Optimization</li>
    <li>Content &amp; Experience Strategy</li>
  </ul>
</section>

</body>
</html>
```